Commercial Loan Originator Business Card (CHANGE COLORS SCHEME)

CHANGE COLOR SCHEME - SAME DESIGN

Name Marissa Lantham
Title Commercial Loan Originator
Office (800) 641-2905 x68
Direct (240) 617-2435
Email brightleaf4you@mailpost.example

Name Derek Fallow
Office (800) 641-2905 x70
Direct (410) 932-1864
Email d.falthebroker@mailpost.example

Name Gordon Wexley
Office (800) 641-2905 x71
Direct (215) 346-2081
Email g.wexley37@mailpost.example

Name Lyn Moreau
Office (800) 641-2905 x
Direct (202) 458-1937
Email lmoreau64@mailpost.example

Name Nadia Strand
Office (800) 641-2905 x72
Direct (240) 871-5246
Email qrzhomelending@mailpost.example

```html
<!DOCTYPE html>
<html lang="en">
<head>
<meta charset="utf-8">
<title>Derek Fallow – Commercial Loan Originator Business Card</title>
<link rel="stylesheet" href="https://fonts.googleapis.com/css2?family=Allura&family=Cormorant+Garamond:wght@500&family=Poppins:wght@300;400;600&display=swap">
<style>
  :root {
    --backdrop: #2b3e52;
    --card: #f4f7f9;
    --band: #d9e4ec;
    --ink: #1e3144;
    --ink-soft: #3f5468;
    --rule: #9fb2c2;
    --icon-mark: #f4f7f9;
    --photo-dark: #35434f;
    --photo-light: #dbe5ec;
  }
  * { margin: 0; padding: 0; box-sizing: border-box; }
  html, body { width: 1010px; height: 1200px; overflow: hidden; }
  body { background: var(--backdrop); position: relative; font-family: "Poppins", sans-serif; color: var(--ink); }

  .card {
    position: absolute; left: 108px; width: 795px; height: 454px;
    background: var(--card); overflow: hidden;
  }
  .card--front { top: 113px; }
  .card--back { top: 633px; }

  .band {
    position: absolute; left: 40px; right: 0; top: 89px; height: 277px;
    background: var(--band); border-radius: 139px 0 0 139px;
  }

  .name-block { position: absolute; text-align: center; color: var(--ink); }
  .name-block .first {
    display: block; font-family: "Allura", cursive; font-weight: 400;
    line-height: 1; position: relative; z-index: 1;
  }
  .name-block .last {
    display: block; font-family: "Cormorant Garamond", serif; font-weight: 500;
    letter-spacing: 0.02em; line-height: 1;
  }
  .name-block .title {
    display: block; font-family: "Poppins", sans-serif; font-weight: 300;
    color: var(--ink-soft); white-space: nowrap;
  }

  .card--front .name-block { left: 118px; width: 300px; top: 146px; }
  .card--front .first { font-size: 112px; margin-bottom: -44px; }
  .card--front .last { font-size: 58px; }
  .card--front .title { font-size: 20px; margin-top: 6px; }

  .portrait {
    position: absolute; left: 441px; top: 36px; width: 310px; height: 418px;
    background: linear-gradient(180deg, var(--photo-light) 0%, var(--photo-dark) 30%, #26313a 100%);
    border-radius: 120px 120px 0 0;
  }

  .card--back .name-block { left: 96px; width: 250px; top: 158px; }
  .card--back .first { font-size: 88px; margin-bottom: -34px; }
  .card--back .last { font-size: 50px; }
  .card--back .title { font-size: 16px; margin-top: 4px; }

  .divider {
    position: absolute; left: 366px; top: 145px; width: 1px; height: 159px;
    background: var(--rule);
  }

  .contact-icons { position: absolute; left: 411px; top: 165px; display: flex; gap: 7px; }
  .contact-icons svg { width: 25px; height: 25px; display: block; }

  .contact-list { position: absolute; left: 409px; top: 209px; list-style: none; }
  .contact-list li { font-size: 18.5px; line-height: 35px; white-space: nowrap; color: var(--ink); }
  .contact-list strong { font-weight: 600; }
  .contact-list .email { font-weight: 600; }
</style>
</head>
<body>

  <section class="card card--front">
    <div class="band"></div>
    <div class="name-block">
      <span class="first">Derek</span>
      <span class="last">FALLOW</span>
      <span class="title">Commercial Loan Originator</span>
    </div>
    <div class="portrait" role="img" aria-label="Portrait photo of Derek Fallow in a dark suit"></div>
  </section>

  <section class="card card--back">
    <div class="band"></div>
    <div class="name-block">
      <span class="first">Derek</span>
      <span class="last">FALLOW</span>
      <span class="title">Commercial Loan Originator</span>
    </div>
    <div class="divider"></div>

    <div class="contact-icons">
      <svg viewBox="0 0 24 24" aria-label="Office">
        <circle cx="12" cy="12" r="12" fill="#1e3144"/>
        <rect x="8" y="6.5" width="5" height="11" fill="none" stroke="#f4f7f9" stroke-width="1.3"/>
        <rect x="13" y="9.5" width="3.5" height="8" fill="none" stroke="#f4f7f9" stroke-width="1.3"/>
        <path d="M9.7 9h1.6M9.7 11.5h1.6M9.7 14h1.6" stroke="#f4f7f9" stroke-width="1.1"/>
      </svg>
      <svg viewBox="0 0 24 24" aria-label="Phone">
        <circle cx="12" cy="12" r="12" fill="#1e3144"/>
        <path d="M8.5 7c-.8.6-1 1.6-.6 2.6 1.2 3 3.5 5.3 6.5 6.5 1 .4 2 .2 2.6-.6l-1.9-1.9-1.5.9c-1.5-.7-2.8-2-3.5-3.5l.9-1.5z" fill="none" stroke="#f4f7f9" stroke-width="1.2" stroke-linejoin="round"/>
      </svg>
      <svg viewBox="0 0 24 24" aria-label="Email">
        <circle cx="12" cy="12" r="12" fill="#1e3144"/>
        <rect x="6.5" y="8" width="11" height="8" rx="1" fill="#f4f7f9"/>
        <path d="M6.8 8.5l5.2 4 5.2-4" fill="none" stroke="#1e3144" stroke-width="1.1"/>
      </svg>
    </div>

    <ul class="contact-list">
      <li><strong>Office</strong> (800) 641-2905 x70</li>
      <li><strong>Direct</strong> (410) 932-1864</li>
      <li class="email">d.falthebroker@mailpost.example</li>
    </ul>
  </section>

</body>
</html>
```